Verantix - Solution provider in business consulting

Verantix is a swiss based company providing solutions for developing markets. The business covers various fields of business consulting, such as supply chain, product costs, quality management and manufacturing management. The Business operates in a efficient, straight and solution oriented manner.
The final design should communicate these characteristics. Asian people as well as as western people shall identify the qualities of the company at first sight.
The customer needs business cards with a simple view but an recognizable design, printed in high quality. Engraved elements such as the globe or simple words are possible.
Available colors are: (RAL)
102/102/102
51/102/102
153/204/153
255/102/51
Font: Calibri
Industry/Entity Type
Business
Look and feel
Each slider illustrates characteristics of the customer's brand and the style your logo design should communicate.

```html
<!DOCTYPE html>
<html lang="en">
<head>
<meta charset="utf-8">
<title>Verantix business cards</title>
<link href="https://fonts.googleapis.com/css2?family=Carlito:wght@400;700&display=swap" rel="stylesheet">
<style>
  :root {
    --page: #e9e7e3;
    --ink: #666666;
    --ink-soft: #8a8a8a;
    --rule: #b5b5b5;
    --paper: #ffffff;
    --back-card: #a3a3a3;
    --band-dark: #8c8c8c;
    --band-light: #c9c9c9;
    --white: #ffffff;
  }
  * { box-sizing: border-box; margin: 0; padding: 0; }
  html, body { width: 1200px; height: 950px; overflow: hidden; }
  body {
    background: var(--page);
    font-family: "Carlito", "Calibri", sans-serif;
    color: var(--ink);
    position: relative;
  }
  .card {
    position: absolute;
    width: 660px;
    height: 377px;
    border-radius: 4px;
    box-shadow: 0 8px 22px rgba(0,0,0,.18);
    overflow: hidden;
  }
  /* Back side */
  .card-back {
    left: 270px;
    top: 60px;
    background: var(--back-card);
    display: flex;
    flex-direction: column;
    align-items: center;
    justify-content: center;
    gap: 26px;
  }
  .card-back .brand-name {
    color: var(--white);
    font-size: 64px;
    font-weight: 400;
    letter-spacing: 1px;
    display: flex;
    align-items: center;
    gap: 14px;
  }
  .brand-dot {
    width: 18px; height: 18px; border-radius: 50%;
    background: currentColor;
    display: inline-block;
  }
  .card-back .web {
    color: var(--white);
    font-size: 17px;
    letter-spacing: 5px;
  }
  /* Front side */
  .card-front {
    left: 270px;
    top: 513px;
    background: var(--paper);
  }
  .front-logo {
    position: absolute;
    right: 58px;
    top: 40px;
    font-size: 56px;
    color: var(--ink);
    letter-spacing: 1px;
    display: flex;
    align-items: center;
    gap: 12px;
  }
  .front-rule {
    position: absolute;
    left: 250px;
    right: 50px;
    top: 128px;
    height: 1px;
    background: var(--rule);
  }
  .company {
    position: absolute;
    right: 50px;
    top: 146px;
    text-align: right;
    font-size: 16px;
    line-height: 1.3;
    color: var(--ink-soft);
  }
  .company .company-name { font-weight: 700; color: var(--ink); }
  .person {
    position: absolute;
    left: 46px;
    top: 218px;
  }
  .person .name { font-size: 23px; font-weight: 700; color: var(--ink); }
  .person .role { font-size: 15px; color: var(--ink-soft); margin-top: 1px; }
  .contacts {
    position: absolute;
    left: 46px;
    top: 278px;
    list-style: none;
    font-size: 15px;
    line-height: 1.22;
    color: var(--ink);
  }
  .contacts li { display: flex; align-items: center; gap: 8px; }
  .contacts svg { width: 13px; height: 13px; fill: var(--ink); flex: none; }
  .edge-band {
    position: absolute;
    left: 0; right: 0; bottom: 0;
    height: 14px;
    display: flex;
    gap: 4px;
  }
  .edge-band .band-main { flex: 1; background: linear-gradient(90deg, var(--band-light), var(--band-dark)); }
  .edge-band .band-end { width: 200px; background: var(--band-light); }
</style>
</head>
<body>

  <section class="card card-back" aria-label="Card back">
    <div class="brand-name">verantix<span class="brand-dot"></span></div>
    <div class="web">www.verantix.ch</div>
  </section>

  <section class="card card-front" aria-label="Card front">
    <div class="front-logo">verantix<span class="brand-dot"></span></div>
    <div class="front-rule"></div>

    <address class="company" style="font-style:normal">
      <div class="company-name">Verantix GmbH</div>
      <div>Feldstrasse 14, 9230 Flawil</div>
      <div>Switzerland</div>
    </address>

    <div class="person">
      <div class="name">Lukas Brenner</div>
      <div class="role">CEO</div>
    </div>

    <ul class="contacts">
      <li>
        <svg viewBox="0 0 16 16" aria-hidden="true"><path d="M3 1h3l1.5 4-2 1.3a9 9 0 0 0 4.2 4.2L11 8.5l4 1.5v3c0 1-1 2-2 2A12 12 0 0 1 1 3c0-1 1-2 2-2z"/></svg>
        +41 71 480 3172
      </li>
      <li>
        <svg viewBox="0 0 16 16" aria-hidden="true"><path d="M4 0h8a1 1 0 0 1 1 1v14a1 1 0 0 1-1 1H4a1 1 0 0 1-1-1V1a1 1 0 0 1 1-1zm1 2v10h6V2zm3 11a1 1 0 1 0 0 2 1 1 0 0 0 0-2z"/></svg>
        +41 79 265 8430
      </li>
      <li>
        <svg viewBox="0 0 16 16" aria-hidden="true"><path d="M0 3h16v1L8 9 0 4zm0 3 8 5 8-5v7H0z"/></svg>
        lukas.brenner@verantix.ch
      </li>
      <li>
        <svg viewBox="0 0 16 16" aria-hidden="true"><path d="M8 0a8 8 0 1 0 0 16A8 8 0 0 0 8 0zm0 1.5c.8 0 1.9 2 2.1 5.5H5.9C6.1 3.5 7.2 1.5 8 1.5zM1.6 9h2.8c.1 2 .5 3.7 1.2 4.9A6.5 6.5 0 0 1 1.6 9zm0-2a6.5 6.5 0 0 1 4-4.9C4.9 3.3 4.5 5 4.4 7zm6.4 7.5c-.8 0-1.9-2-2.1-5.5h4.2c-.2 3.5-1.3 5.5-2.1 5.5zm2.4-.6c.7-1.2 1.1-2.9 1.2-4.9h2.8a6.5 6.5 0 0 1-4 4.9zM11.6 7c-.1-2-.5-3.7-1.2-4.9a6.5 6.5 0 0 1 4 4.9z"/></svg>
        www.verantix.ch
      </li>
    </ul>

    <div class="edge-band" aria-hidden="true">
      <div class="band-main"></div>
      <div class="band-end"></div>
    </div>
  </section>

</body>
</html>
```